依頼詳細
新規オープンする癒しサロンの名刺作成をお願いします。
代表者と店員が使用します。

○「優しさ」「穏やかさ」「暖かみ」を感じるデザイン
○添付したロゴを使用してください。(型抜きなどの加工可、分解した部分使用不可)
○名刺全体が黒や暗色になったものは避けてください。
○ラベンダーなどの、フリー画像、挿絵を使用していただいても結構です。
○表:フルカラー または、表:フルカラー 裏:1色 このどちらかでお願いします。
記載項目
○店舗名 : ミストベール
○肩書き : 代表
○氏名 : 高橋 五月
○住所 : 〒394-0051 長野県岡谷市栄町2丁目**-*
○TEL/FAX : 0266-47-****
○URL : http://mistveil-salon.example
○E-Mail : info@mistveil-salon.example

○資格 :KPRB認定スポーツアロマトレーナー
NOGW認定アロマテラピーインストラクター
NOGW認定アロマセラピスト
BRUKO認定ハーバルセラピスト
希望イメージ
シンプル 複雑
単色 カラフル
暗い 明るい
日常 高級
遊び心 厳粛
未来的 伝統的
女性的 男性的
希望する色
緑、オレンジ、その他アロマやハーブを連想できる明るい色
納品ファイル
• イラストレーター形式 (.ai)
補足説明

```html
<!DOCTYPE html>
<html lang="ja">
<head>
<meta charset="utf-8">
<title>ミストベール 名刺</title>
<link rel="stylesheet" href="https://fonts.googleapis.com/css2?family=Noto+Sans:wght@400&family=Noto+Serif+JP:wght@400;500&display=swap">
<style>
  :root {
    --paper-top: #f1eaf6;
    --paper-bottom: #f7eef5;
    --lavender-text: #98a6dc;
    --gold: #b8913a;
    --ink: #3a3340;
    --feather-main: #b7b4e6;
    --feather-soft: #e3d3ee;
    --accent-pink: #d59ac4;
  }
  html, body {
    margin: 0;
    padding: 0;
    overflow: hidden;
    background: #ffffff;
  }
  .card {
    position: relative;
    width: 742px;
    height: 1200px;
    overflow: hidden;
    background: linear-gradient(180deg, var(--paper-top) 0%, #f6f1f9 45%, var(--paper-bottom) 100%);
    font-family: "Noto Serif JP", serif;
    color: var(--ink);
  }
  .salon-tagline {
    position: absolute;
    top: 18px;
    left: 0;
    width: 100%;
    text-align: center;
    font-family: "Noto Sans", sans-serif;
    font-size: 40px;
    color: var(--lavender-text);
    letter-spacing: 0.5px;
    margin: 0;
  }
  .feather-art {
    position: absolute;
    left: 120px;
    top: 190px;
    width: 622px;
    height: 440px;
  }
  .brand-mark {
    position: absolute;
    top: 200px;
    left: 76px;
    width: 440px;
    margin: 0;
    text-align: center;
    color: var(--gold);
    font-family: "Noto Serif JP", serif;
    font-weight: 500;
    font-size: 64px;
    line-height: 1.2;
    letter-spacing: 1px;
  }
  .shop-name {
    position: absolute;
    top: 604px;
    left: 0;
    width: 100%;
    padding-left: 90px;
    box-sizing: border-box;
    text-align: center;
    font-size: 40px;
    font-weight: 400;
    letter-spacing: 2px;
    margin: 0;
  }
  .person {
    position: absolute;
    top: 670px;
    left: 0;
    width: 100%;
    padding-left: 100px;
    box-sizing: border-box;
    text-align: center;
  }
  .person .title-name {
    font-size: 30px;
    letter-spacing: 3px;
    line-height: 1.2;
  }
  .person .title-name .role {
    margin-right: 22px;
  }
  .person .romaji {
    font-size: 18px;
    letter-spacing: 1px;
    margin-top: 2px;
  }
  .qualifications {
    position: absolute;
    top: 748px;
    left: 0;
    width: 100%;
    padding: 0 0 0 90px;
    box-sizing: border-box;
    list-style: none;
    margin: 0;
    text-align: center;
    font-size: 26px;
    line-height: 32px;
  }
  .divider-mark {
    position: absolute;
    top: 882px;
    left: 455px;
    width: 16px;
    height: 16px;
    background: var(--accent-pink);
  }
  .contact {
    position: absolute;
    top: 905px;
    left: 180px;
    font-size: 23px;
    line-height: 32px;
    margin: 0;
    font-style: normal;
  }
  .contact span { display: block; }
  .contact .url { padding-left: 56px; }
</style>
</head>
<body>
  <main class="card">
    <p class="salon-tagline">Salon healing mistveil</p>

    <svg class="feather-art" viewBox="0 0 622 440" role="img" aria-label="Large soft lavender feather with flowing fine-line waves and small gold sparkles">
      <defs>
        <radialGradient id="featherGlow" cx="55%" cy="50%" r="60%">
          <stop offset="0%" stop-color="#b7b4e6" stop-opacity="0.85"/>
          <stop offset="60%" stop-color="#e3d3ee" stop-opacity="0.6"/>
          <stop offset="100%" stop-color="#f1eaf6" stop-opacity="0"/>
        </radialGradient>
      </defs>
      <ellipse cx="330" cy="230" rx="300" ry="200" fill="url(#featherGlow)"/>
    </svg>

    <p class="brand-mark">Mist Veil</p>

    <h1 class="shop-name">ミストベール</h1>

    <div class="person">
      <div class="title-name"><span class="role">代表</span>高橋 五月</div>
      <div class="romaji">satsuki takahashi</div>
    </div>

    <ul class="qualifications">
      <li>KPRB 認定スポーツアロマトレーナー</li>
      <li>NOGW 認定アロマテラピーインストラクター</li>
      <li>NOGW 認定アロマセラピスト</li>
      <li>BRUKO 認定ハーバルセラピスト</li>
    </ul>

    <div class="divider-mark"></div>

    <address class="contact">
      <span>〒394-0051　長野県岡谷市栄町2丁目**-*</span>
      <span>Tel.0266-47-****　Fax.0266-47-****</span>
      <span class="url">URL　http://mistveil-salon.example</span>
      <span class="url">E-Mail info@mistveil-salon.example</span>
    </address>
  </main>
</body>
</html>
```